Tarvel Ridge LLC

Need Professional Business cards for New Investment Fund

Target Market(s)

High Quality investors

Industry/Entity Type

Financial

Contact Information for Business Card

Phone Number +1 555 284 6193
Name Pavel Orlinsky
Title Fund Manager
email po@FundTarvel.example
Website www.FundTarvel.example

Colors

Designer to choose colors to be used in the design.

Requirements
Must have
• Must have our Logo and all of the above. Must be made so lettering and loge can be raised

```html
<!DOCTYPE html>
<html lang="en">
<head>
<meta charset="utf-8">
<title>Tarvel Ridge LLC — Business Card</title>
<link rel="stylesheet" href="https://fonts.googleapis.com/css2?family=Didact+Gothic&family=Montserrat:wght@700&display=swap">
<style>
  :root {
    --stage: #161616;
    --card: #262626;
    --card-light: #363636;
    --accent: #22e01e;
    --text-light: #f2f2f2;
    --text-muted: #9a9a9a;
  }
  * { box-sizing: border-box; margin: 0; padding: 0; }
  html, body {
    width: 1200px; height: 900px; overflow: hidden;
    background: var(--stage);
  }
  .canvas {
    width: 1200px; height: 900px;
    display: flex; flex-direction: column; align-items: center; justify-content: center;
    gap: 30px;
  }
  .card {
    position: relative;
    width: 700px; height: 390px;
    background: radial-gradient(ellipse at 70% 40%, var(--card-light) 0%, var(--card) 60%);
    box-shadow: 0 12px 30px rgba(0,0,0,0.6);
    overflow: hidden;
  }
  .card::after {
    content: ""; position: absolute; left: 0; right: 0; bottom: 0;
    height: 7px; background: var(--accent);
  }
  .wordmark {
    display: flex; align-items: center; gap: 12px;
    font-family: "Didact Gothic", sans-serif;
    font-size: 34px; letter-spacing: 1px;
  }
  .wordmark-mark { width: 18px; height: 18px; }
  .card-back { display: flex; align-items: center; justify-content: center; }
  .card-back .wordmark { color: var(--text-muted); }
  .card-back .wordmark-mark { background: var(--text-muted); }

  .card-front { display: flex; align-items: center; }
  .card-front .wordmark {
    color: var(--text-light); width: 290px; justify-content: center; font-size: 30px;
  }
  .card-front .wordmark-mark { background: var(--accent); }
  .divider {
    width: 2px; height: 150px; background: var(--accent); margin-right: 40px;
  }
  .contact { font-family: "Didact Gothic", sans-serif; color: var(--text-light); }
  .person-name {
    font-family: "Montserrat", sans-serif; font-weight: 700;
    font-size: 27px; color: var(--accent); line-height: 1.1;
  }
  .person-title { font-size: 21px; margin-bottom: 22px; }
  .contact-list { list-style: none; font-size: 21px; line-height: 1.45; }
  .contact-list li { display: flex; align-items: center; gap: 12px; }
  .contact-list svg { width: 16px; height: 16px; flex: none; }
  .highlight { color: var(--accent); }
</style>
</head>
<body>
<main class="canvas">
  <section class="card card-back" aria-label="Card back">
    <div class="wordmark"><span class="wordmark-mark"></span>Tarvel Ridge</div>
  </section>

  <section class="card card-front" aria-label="Card front">
    <div class="wordmark"><span class="wordmark-mark"></span>Tarvel Ridge</div>
    <div class="divider"></div>
    <div class="contact">
      <p class="person-name">Pavel Orlinsky</p>
      <p class="person-title">Fund Manager</p>
      <ul class="contact-list">
        <li>
          <svg viewBox="0 0 16 16" aria-hidden="true"><path d="M4 1.5 6 4.5 4.8 6c.8 2 2.6 3.8 4.5 4.6l1.5-1.2 3 2-1.3 2.4C8.2 13.6 2.4 7.8 1.6 2.8Z" fill="none" stroke="var(--accent)" stroke-width="1.4" stroke-linejoin="round"/></svg>
          +1 555 284 6193
        </li>
        <li>
          <svg viewBox="0 0 16 16" aria-hidden="true"><rect x="1.5" y="3.5" width="13" height="9" fill="none" stroke="var(--accent)" stroke-width="1.4"/><path d="M1.5 3.5 8 9l6.5-5.5" fill="none" stroke="var(--accent)" stroke-width="1.4"/></svg>
          po@FundTarvel.example
        </li>
        <li>
          <svg viewBox="0 0 16 16" aria-hidden="true"><circle cx="8" cy="8" r="6.5" fill="none" stroke="var(--accent)" stroke-width="1.4"/><ellipse cx="8" cy="8" rx="2.8" ry="6.5" fill="none" stroke="var(--accent)" stroke-width="1.2"/><path d="M1.5 8h13M2.5 5h11M2.5 11h11" stroke="var(--accent)" stroke-width="1.1"/></svg>
          <span>www.<span class="highlight">FundTarvel</span>.example</span>
        </li>
      </ul>
    </div>
  </section>
</main>
</body>
</html>
```